Northern Guild of Acute Care Doctors Membership Poster Design

We need a poster that highlights why physicians should become a member of our association.

As the national voice of emergency medicine (EM), NGAD provides continuing medical education, advocates on behalf of emergency physicians and their patients, supports research and strengthens the EM community. In co-operation with other specialties and committees, NGAD also plays a vital role in the development of national standards and clinical guidelines.

NGAD keeps Canadian emergency physicians informed of developments in the clinical practice of EM and addresses political and societal changes, that affect the delivery of emergency health care.

Vision
Leading excellence in Emergency Medicine across Canada

Mission
NGAD champions excellence in Emergency Medicine in Canada by:

Advocating for Emergency Physicians and their patients;
Connecting Emergency Physicians;
Leading Emergency Medicine education;
Fostering research and innovation
Defining standards for quality Emergency Care
Collaborating with Emergency Care providers.

Target Market(s)

Physicians, Residents and Medical Students

Industry/Entity Type

Doctor

Font styles to use
Sans Serif

Requirements
Must have
• Why belong?
• Career Development
• Vision
• Leading excellence in Emergency Medicine across Canada
• Mission
• NGAD champions excellence in Emergency Medicine in Canada by:
• Advocating for Emergency Physicians and their patients;
• Connecting Emergency Physicians;
• Leading Emergency Medicine education;
• Fostering research and innovation
• Defining standards for quality Emergency Care
• Collaborating with Emergency Care providers.
• Financial Discounts
• Special rates at Brellwick Inns
• Discount on fares from Trelo Trains
• Discounts on home and auto insurance thought the Halvesta Group and Prudora Choice
• Special rates on medical and dental insurance through Bluefen Cover Canada
• Special rates with Kestrin Mobile or Vomba
• Discounts on tickets from Olstander Stageworks
• Discounts on tickets from Marquee Tours Nationwide
• Advocacy
• NGAD advocates on behalf of you and your patients
• We support the development of the specialty of emergency medicine for you
• Gain a larger voice representing you and your specialty
• Networking Opportunities
• Opportunity to become involved with NGAD committees and sections
• Connect with colleagues and potential mentors at events and through online discussions
• Member Types
• Physician Members
• Resident Members
• Student Members
• Associate Members
• ngad-example.ca
• Corporate colours or colours that are complimentary to our corporate colours
• Hex 0077b2
• Hex DF0631
Nice to have
• Pictures

```html
<!DOCTYPE html>
<html lang="en">
<head>
<meta charset="utf-8">
<title>Why Belong? – Northern Guild of Acute Care Doctors</title>
<link rel="stylesheet" href="https://fonts.googleapis.com/css2?family=Open+Sans:ital,wght@0,300;0,400;0,700;1,400;1,700&family=Playfair+Display:ital,wght@1,700&display=swap">
<style>
  :root {
    --brand-blue: #0077b2;
    --brand-red: #df0631;
    --deep-red: #8c1424;
    --ink: #1f2a33;
    --panel: rgba(255,255,255,0.9);
    --photo-dark: #2f5666;
    --photo-mid: #6f9aa6;
    --photo-light: #c9dde2;
  }
  html, body { margin: 0; padding: 0; overflow: hidden; }
  body { width: 1200px; height: 2216px; position: relative; background: #fff; font-family: "Open Sans", Arial, sans-serif; color: var(--ink); }

  .poster { position: absolute; inset: 0; overflow: hidden; }

  .backdrop-photo {
    position: absolute; left: 0; top: 0; width: 1200px; height: 2216px;
    background: linear-gradient(180deg, var(--photo-light) 0%, var(--photo-mid) 12%, var(--photo-dark) 30%, #4b6f7a 65%, #9fb8bf 100%);
  }
  .stethoscope-photo {
    position: absolute; left: 760px; top: 1560px; width: 440px; height: 656px;
    background: radial-gradient(ellipse at 60% 55%, #eef2f4 0%, #c3d1d6 45%, rgba(120,150,160,0.5) 80%, rgba(120,150,160,0) 100%);
  }

  .headline {
    position: absolute; left: 0; top: 6px; width: 1200px; text-align: center; margin: 0;
    font-family: "Playfair Display", Georgia, serif; font-style: italic; font-weight: 700;
    font-size: 178px; line-height: 1; color: var(--brand-red); letter-spacing: 4px;
  }
  .subhead-band {
    position: absolute; left: 0; top: 158px; width: 1200px; height: 76px;
    background: rgba(255,255,255,0.45);
  }
  .subhead {
    position: absolute; left: 0; top: 158px; width: 1200px; text-align: center; margin: 0;
    font-weight: 300; font-size: 62px; letter-spacing: 11px; color: var(--brand-blue); line-height: 76px;
  }

  .content-panel {
    position: absolute; left: 16px; top: 636px; width: 1090px; height: 1470px;
    background: var(--panel);
  }
  .rule-top { position: absolute; left: 16px; top: 648px; width: 864px; height: 4px; background: var(--brand-red); }
  .rule-side { position: absolute; left: 40px; top: 648px; width: 4px; height: 192px; background: var(--brand-red); }

  .red-cross { position: absolute; left: 900px; top: 664px; width: 200px; height: 200px; }

  .section-title {
    position: absolute; left: 60px; margin: 0;
    font-weight: 700; font-size: 56px; letter-spacing: 3px; color: var(--brand-red); line-height: 60px;
  }
  .vision-title { top: 660px; }
  .mission-title { top: 836px; }

  .vision-text {
    position: absolute; left: 60px; top: 720px; width: 700px; margin: 0;
    font-style: italic; font-size: 32px; line-height: 38px;
  }
  .mission-lead {
    position: absolute; left: 60px; top: 896px; width: 1000px; margin: 0;
    font-style: italic; font-size: 33px; line-height: 40px;
  }
  .mission-list {
    position: absolute; left: 60px; top: 1010px; width: 1000px; margin: 0; padding: 0; list-style: none;
    font-style: italic; font-weight: 700; font-size: 33px; line-height: 36px; letter-spacing: 1px;
  }

  .benefit-list {
    position: absolute; left: 60px; top: 1348px; width: 980px; margin: 0; padding: 0; list-style: none;
    font-size: 23px; line-height: 28px; color: var(--deep-red);
  }
  .benefit-list .group { font-weight: 700; }

  .footer-band { position: absolute; left: 0; top: 2106px; width: 1200px; height: 110px; background: rgba(255,255,255,0.92); }
  .guild-mark { position: absolute; left: 30px; top: 2122px; display: flex; align-items: center; gap: 12px; }
  .guild-mark .dot { width: 44px; height: 44px; border-radius: 50%; background: var(--brand-red); }
  .guild-mark .name { font-weight: 700; font-size: 40px; color: var(--brand-red); letter-spacing: 2px; line-height: 1; }
  .web-address {
    position: absolute; left: 300px; top: 2140px; width: 800px; text-align: center; margin: 0;
    font-weight: 700; font-size: 38px; letter-spacing: 7px; color: var(--brand-red); line-height: 50px;
  }
</style>
</head>
<body>
<div class="poster">
  <div class="backdrop-photo" role="img" aria-label="Photo of an operating room with surgical lights and a surgeon in teal scrubs"></div>
  <div class="stethoscope-photo" role="img" aria-label="Photo of a stethoscope resting on a medical chart"></div>

  <h1 class="headline">Why Belong?</h1>
  <div class="subhead-band"></div>
  <p class="subhead">CAREER DEVELOPMENT</p>

  <div class="content-panel"></div>
  <div class="rule-top"></div>
  <div class="rule-side"></div>

  <svg class="red-cross" viewBox="0 0 200 200" aria-hidden="true">
    <rect x="67" y="0" width="66" height="200" fill="#df0631"/>
    <rect x="0" y="67" width="200" height="66" fill="#df0631"/>
  </svg>

  <h2 class="section-title vision-title">VISION</h2>
  <p class="vision-text">Leading excellence<br>in Emergency Medicine<br>across Canada</p>

  <h2 class="section-title mission-title">MISSION</h2>
  <p class="mission-lead">NGAD champions excellence in Emergency<br>Medicine in Canada by:</p>
  <ul class="mission-list">
    <li>-Advocating for Emergency</li>
    <li>-Physicians and their patients;</li>
    <li>-Connecting Emergency Physicians;</li>
    <li>-Leading Emergency Medicine education;</li>
    <li>-Fostering research and innovation;</li>
    <li>-Defining standards for quality Emergency</li>
    <li>&nbsp;&nbsp;Care;</li>
    <li>-Collaborating with Emergency Care</li>
    <li>&nbsp;&nbsp;providers.</li>
  </ul>

  <ul class="benefit-list">
    <li class="group">- Financial Discounts</li>
    <li>- Special rates at Brellwick Inns</li>
    <li>- Discount on fares from Trelo Trains</li>
    <li>- Discounts on home and auto insurance thought the Halvesta Group and Prudora Choice</li>
    <li>- Special rates on medical and dental insurance through Bluefen Cover Canada</li>
    <li>- Special rates with Kestrin Mobile or Vomba</li>
    <li>- Discounts on tickets from Olstander Stageworks</li>
    <li>- Discounts on tickets from Marquee Tours Nationwide</li>
    <li class="group">- Advocacy</li>
    <li>- NGAD advocates on behalf of you and your patients</li>
    <li>- We support the development of the specialty of emergency medicine for you</li>
    <li>- Gain a larger voice representing you and your specialty</li>
    <li class="group">- Networking Opportunities</li>
    <li>- Opportunity to become involved with NGAD committees and sections</li>
    <li>- Connect with colleagues and potential mentors at events and through online discussions</li>
    <li class="group">- Member Types</li>
    <li>- Physician Members</li>
    <li>- Resident Members</li>
    <li>- Student Members</li>
    <li>- Associate Members</li>
  </ul>

  <div class="footer-band"></div>
  <div class="guild-mark"><span class="dot"></span><span class="name">NGAD</span></div>
  <p class="web-address">WWW.NGAD-EXAMPLE.CA</p>
</div>
</body>
</html>
```